New Web Design Project open cart

We are about to start a new furniture selling website and it will be based on open cart . we mainly need two pages designing landing page & item page. so come up with your unique ideas and designs . Please make sure the design needs to be unique . no templates and themes . Will make the selected designer even happier if your design is selected. So basically over all it is going to be the new theme for our open cart base eCommerce website .we will appreciate if its responsive with some unique features .
SO as per request of designers about more brief about the project = WE ONLY NEED A RESPONSIVE THEME FOR OUR OPEN CART BASE eCommerce WebSite . Mainly item page & product page needs a good unique design. Lighter, speed load, compatible with all browsers and responsive will be appreciated . To Get an idea check on loungerix .co .uk website or tablowmeadows etc.
more projects coming soon .

Our audience will be furniture buying customers .

Furniture

• to get some sort of idea have a look at loungerix .co uk`s website`s listing page and landing page .
• responsive, easy to customize, full theme .

```html
<!DOCTYPE html>
<html lang="en">
<head>
<meta charset="utf-8">
<title>Oakhaven – Categories</title>
<link href="https://fonts.googleapis.com/css2?family=Lato:ital,wght@0,400;0,700;0,900;1,400&display=swap" rel="stylesheet">
<style>
:root{
  --pink:#d91c4e;
  --pink-dark:#b5133e;
  --teal:#1a9db0;
  --teal-dark:#137f8f;
  --green:#7bb02c;
  --ink:#222;
  --muted:#555;
  --line:#d6d6d6;
  --footer:#2b2b2b;
}
*{box-sizing:border-box;margin:0;padding:0}
html,body{width:854px;height:1200px;overflow:hidden;background:#fff;font-family:'Lato',sans-serif;color:var(--ink)}
.page{position:relative;width:854px;height:1200px}
.abs{position:absolute}
/* header */
.logo{left:93px;top:14px;display:flex;align-items:center;gap:8px}
.logo-mark{width:30px;height:30px;background:var(--pink);border-radius:6px}
.logo-name{font-size:34px;font-weight:700;color:var(--ink);letter-spacing:-.5px}
.auth{left:620px;top:0;width:140px;height:26px;background:var(--green);display:flex;color:#fff;font-size:10px}
.auth span{flex:1;display:flex;align-items:center;justify-content:center;gap:5px}
.auth span+span{border-left:1px solid #5f8d1e}
.toplinks{left:510px;top:43px;display:flex;gap:14px;font-size:9.5px;color:#333}
.toplinks span+span{border-left:1px solid #ccc;padding-left:14px}
.search{left:437px;top:72px;width:205px;height:26px;border:1px solid var(--line);font-size:8.5px;color:#666;padding:8px}
.search svg{position:absolute;right:7px;top:7px}
.cart{left:649px;top:72px;width:111px;height:26px;border:1px solid var(--line);font-size:9.5px;font-weight:700;display:flex;align-items:center;justify-content:center;gap:5px}
.nav{left:0;top:110px;width:854px;height:33px;background:linear-gradient(var(--pink),var(--pink-dark));display:flex;padding-left:93px}
.nav a{color:#fff;font-size:11px;text-decoration:none;display:flex;align-items:center;padding:0 21px;position:relative}
.nav a+a::before{content:"";position:absolute;left:0;top:10px;height:13px;border-left:1px solid rgba(255,255,255,.35)}
.nav a.active{background:var(--teal);padding:0 23px}
.crumb{left:93px;top:159px;font-size:8.5px}
.title{left:93px;top:183px;font-size:17px}
.rule{left:93px;top:208px;width:667px;border-top:1px solid var(--line)}
/* sidebar */
.side{left:93px;top:223px;width:167px;border:1px solid var(--line);border-top:0}
.side h3{background:var(--pink);color:#fff;font-weight:400;font-size:15px;height:30px;padding:6px 9px}
.side li{list-style:none;height:26.7px;border-top:1px solid var(--line);font-size:9.5px;padding:8px 0 0 22px;position:relative;color:#333}
.side li::before{content:"›";position:absolute;left:10px;top:5px;font-size:12px}
.side li.on{background:var(--teal);color:#fff}
.sort{left:632px;top:224px;width:75px;height:20px;border:1px solid var(--line);font-size:8.5px;font-style:italic;padding:5px 6px;color:#444}
.sort b{position:absolute;right:0;top:0;width:18px;height:18px;background:#666}
.sort b::after{content:"";position:absolute;left:5px;top:7px;border:4px solid transparent;border-top:5px solid #fff}
.views{left:726px;top:228px;display:flex;gap:8px}
/* grid */
.grid{left:277px;top:257px;width:483px;display:grid;grid-template-columns:repeat(3,157px);gap:8px 6px}
.card{height:201px;border:1px solid var(--line);padding:6px 6px 0}
.photo{height:104px;margin:0 10px}
.chair{background:radial-gradient(ellipse at center,#8a4a2a 0 30%,#fff 62%)}
.sofa{background:radial-gradient(ellipse at center,#4a2a1c 0 45%,#fff 72%)}
.table{background:radial-gradient(ellipse at center,#3c2c26 0 40%,#fff 70%)}
.price{font-size:12px;margin:14px 0 0 0;color:#333}
.name{font-size:10.5px;font-weight:700;margin-top:12px}
.btn{display:inline-flex;align-items:center;gap:7px;margin-top:11px;background:var(--teal);color:#fff;font-size:9px;font-weight:700;height:22px;padding:0 8px;border-bottom:2px solid var(--teal-dark)}
/* pagination */
.pager{left:403px;top:909px;display:flex;gap:5px;font-size:8.5px;align-items:flex-end}
.pager span{border:1px solid #999;height:15px;padding:1px 4px;min-width:15px;text-align:center}
.pager span.cur{background:#222;color:#fff;border-color:#222}
.pager i{font-style:normal;border:0}
.stripe{left:93px;top:964px;width:667px;height:5px;background:repeating-linear-gradient(135deg,#ddd 0 2px,#fff 2px 4px)}
.brands{left:93px;top:993px;width:667px;display:flex;justify-content:space-between;font-size:13px;font-weight:700;color:#222}
/* footer */
.footer{left:0;top:1036px;width:854px;height:136px;background:var(--footer);color:#ddd}
.col{position:absolute;top:12px}
.col h4{font-weight:400;font-size:13.5px;color:#fff;padding-bottom:6px;border-bottom:1px solid #444;margin-bottom:5px}
.col li{list-style:none;font-size:9.5px;height:21px;padding-left:8px;position:relative}
.col li::before{content:"›";position:absolute;left:0;top:-2px;font-size:11px}
.col p{font-size:9px;line-height:1.4;color:#ccc}
.email{margin-top:8px;width:138px;height:19px;background:#fff;color:#777;font-size:7.5px;padding:5px 6px}
.sub{margin-top:8px;display:inline-block;background:#ddd;color:#222;font-size:9px;font-weight:700;padding:4px 8px}
.social li{padding-left:22px;height:25px}
.social li::before{content:"";width:15px;height:15px;background:#fff;top:-3px}
.bottom{left:0;top:1172px;width:854px;height:28px;background:var(--pink);color:#fff;font-size:9.5px;padding:8px 95px}
.cards{position:absolute;right:95px;top:6px;display:flex;gap:3px}
.cards i{width:26px;height:16px;background:#fff;border-radius:2px}
</style>
</head>
<body>
<div class="page">
  <div class="abs logo"><div class="logo-mark"></div><div class="logo-name">Oakhaven</div></div>
  <div class="abs auth"><span>&#128274; Login</span><span>Register</span></div>
  <div class="abs toplinks"><span>My Account</span><span>♡ My Wishlist</span><span>Checkout</span></div>
  <div class="abs search">Search<svg width="11" height="11" viewBox="0 0 12 12"><circle cx="5" cy="5" r="4" fill="none" stroke="#555" stroke-width="1.5"/><line x1="8" y1="8" x2="11" y2="11" stroke="#555" stroke-width="1.5"/></svg></div>
  <div class="abs cart">Shopping Cart ⌄</div>
  <nav class="abs nav"><a class="active">HOME</a><a>BEDROOM</a><a>LIVING ROOM</a><a>DINING ROOM</a><a>KIDS ROOMS</a><a>BRANDS</a><a>SALE</a></nav>
  <div class="abs crumb">Home &nbsp;» &nbsp;Categories</div>
  <h1 class="abs title" style="font-weight:400">Categories</h1>
  <div class="abs rule"></div>

  <aside class="abs side"><h3>Categories</h3><ul>
    <li>Bedroom</li><li>Living Room</li><li class="on">Dining Room</li><li>Kids Rooms</li><li>Furniture</li><li>Wardrobes</li><li>Bookcases</li><li>TV Units</li><li>Accessories</li></ul></aside>

  <div class="abs sort">Short By<b></b></div>
  <div class="abs views"><svg width="14" height="11"><g fill="#666"><rect y="0" width="14" height="2"/><rect y="4.5" width="14" height="2"/><rect y="9" width="14" height="2"/></g></svg><svg width="11" height="11"><g fill="#666"><rect width="5" height="5"/><rect x="6" width="5" height="5"/><rect y="6" width="5" height="5"/><rect x="6" y="6" width="5" height="5"/></g></svg></div>

  <div class="abs grid">
    <div class="card"><div class="photo chair" role="img" aria-label="Wooden dining chair with cream seat"></div><div class="price">$100.95</div><div class="name">Lorem ipsum dolor sit amet</div><div class="btn">🛒 ADD TO CART</div></div>
    <div class="card"><div class="photo sofa" role="img" aria-label="Brown sectional sofa with ottoman"></div><div class="price">$100.95</div><div class="name">Lorem ipsum dolor sit amet</div><div class="btn">🛒 ADD TO CART</div></div>
    <div class="card"><div class="photo table" role="img" aria-label="Dark wood dining table with four chairs"></div><div class="price">$100.95</div><div class="name">Lorem ipsum dolor sit amet</div><div class="btn">🛒 ADD TO CART</div></div>
    <div class="card"><div class="photo chair" role="img" aria-label="Wooden dining chair with cream seat"></div><div class="price">$100.95</div><div class="name">Lorem ipsum dolor sit amet</div><div class="btn">🛒 ADD TO CART</div></div>
    <div class="card"><div class="photo sofa" role="img" aria-label="Brown sectional sofa with ottoman"></div><div class="price">$100.95</div><div class="name">Lorem ipsum dolor sit amet</div><div class="btn">🛒 ADD TO CART</div></div>
    <div class="card"><div class="photo table" role="img" aria-label="Dark wood dining table with four chairs"></div><div class="price">$100.95</div><div class="name">Lorem ipsum dolor sit amet</div><div class="btn">🛒 ADD TO CART</div></div>
    <div class="card"><div class="photo chair" role="img" aria-label="Wooden dining chair with cream seat"></div><div class="price">$100.95</div><div class="name">Lorem ipsum dolor sit amet</div><div class="btn">🛒 ADD TO CART</div></div>
    <div class="card"><div class="photo sofa" role="img" aria-label="Brown sectional sofa with ottoman"></div><div class="price">$100.95</div><div class="name">Lorem ipsum dolor sit amet</div><div class="btn">🛒 ADD TO CART</div></div>
    <div class="card"><div class="photo table" role="img" aria-label="Dark wood dining table with four chairs"></div><div class="price">$100.95</div><div class="name">Lorem ipsum dolor sit amet</div><div class="btn">🛒 ADD TO CART</div></div>
  </div>

  <div class="abs pager"><span>« Previous</span><span class="cur">1</span><span>2</span><span>3</span><span>4</span><span>5</span><i>.....</i><span>10</span><span>Next »</span></div>

  <div class="abs stripe"></div>
  <div class="abs brands"><span>Stonemark</span><span>Beamwork</span><span>lumen</span><span>Palewood</span><span>Vestra</span><span>Ordella</span><span>Kindlecroft</span><span>Meadowline</span></div>

  <footer class="abs footer">
    <div class="col" style="left:102px;width:78px"><h4>Products</h4><ul><li>Bedroom</li><li>Living Room</li><li>Dining Room</li><li>Kids Rooms</li></ul></div>
    <div class="col" style="left:222px;width:92px"><h4>Information</h4><ul><li>Home</li><li>About Us</li><li>Blog</li><li>Contact us</li></ul></div>
    <div class="col" style="left:356px;width:92px"><h4>Your Account</h4><ul><li>Order Status</li><li>My Wishlist</li><li>Order History</li><li>Newsletter</li></ul></div>
    <div class="col" style="left:489px;width:140px"><h4>Newsletter Sign Up</h4><p>Lorem ipsudolor sit ec adipiscing elitsite amet</p><div class="email">Email Address</div><div class="sub">SUBSCRIBE</div></div>
    <div class="col social" style="left:670px;width:90px"><h4>Follow us</h4><ul><li>Friendbook</li><li>Chirper</li><li>Circles+</li></ul></div>
  </footer>
  <div class="abs bottom">© Copyright 2014 Oakhaven. All Right Reserved<div class="cards"><i></i><i></i><i></i><i></i><i></i></div></div>
</div>
</body>
</html>
```